Realty Group Needs Classy, Contemporary Letterhead Design

We need a letterhead design for a new realty company located in NY, USA. We buy investment properties to rehabilitate and or keep in our rental portfolio.

```html
<!DOCTYPE html>
<html lang="en">
<head>
<meta charset="utf-8">
<title>Meridian Realty Group — Letterhead</title>
<link href="https://fonts.googleapis.com/css2?family=Figtree:wght@400;600;700&family=Jost:wght@300;400&display=swap" rel="stylesheet">
<style>
  :root {
    --brand-purple: #4e2d84;
    --ink: #1d1d1f;
    --muted: #6a6a6e;
    --paper: #ffffff;
    --backdrop: #e9ecee;
    --signature-tone: #b7b3c4;
  }
  * { box-sizing: border-box; margin: 0; padding: 0; }
  html, body { width: 1200px; height: 1200px; overflow: hidden; }
  body {
    background: var(--backdrop);
    font-family: "Figtree", "Helvetica Neue", Arial, sans-serif;
    color: var(--ink);
    position: relative;
  }
  .letterhead {
    position: absolute;
    left: 190px; top: 20px;
    width: 820px; height: 1160px;
    background: var(--paper);
  }
  .side-band {
    position: absolute;
    left: 762px; top: 0;
    width: 26px; height: 100%;
    background: var(--brand-purple);
  }
  .brand {
    position: absolute;
    left: 59px; top: 100px;
    display: flex;
    align-items: center;
    gap: 14px;
  }
  .brand-square {
    width: 22px; height: 22px;
    background: var(--brand-purple);
  }
  .brand-name {
    font-weight: 600;
    font-size: 32px;
    line-height: 1;
    color: var(--brand-purple);
    white-space: nowrap;
  }
  .letter-date {
    position: absolute;
    right: 111px; top: 280px;
    font-weight: 700;
    font-size: 14px;
    color: var(--brand-purple);
    padding-bottom: 4px;
    border-bottom: 1.5px solid var(--brand-purple);
  }
  .letter-body {
    position: absolute;
    left: 59px; top: 320px;
    width: 650px;
    font-size: 14px;
    line-height: 29.6px;
  }
  .letter-body p + p { margin-top: 29.6px; }
  .line {
    display: block;
    text-align: justify;
    text-align-last: justify;
    white-space: nowrap;
  }
  .line-last {
    display: block;
    text-align: left;
    white-space: nowrap;
  }
  .signature-mark {
    position: absolute;
    left: 59px; top: 818px;
    width: 135px; height: 30px;
  }
  .signatory {
    position: absolute;
    left: 59px; top: 856px;
  }
  .signatory-name {
    font-weight: 700;
    font-size: 14px;
    color: var(--brand-purple);
    line-height: 1.2;
  }
  .signatory-role {
    font-size: 11.5px;
    color: var(--muted);
    line-height: 1.2;
  }
  .contact-list {
    position: absolute;
    right: 0; top: 0;
    width: 100%; height: 100%;
    list-style: none;
    font-family: "Jost", "Futura", sans-serif;
    font-weight: 300;
    font-size: 12px;
    color: var(--muted);
  }
  .contact-item {
    position: absolute;
    right: 72px;
    text-align: right;
    line-height: 1.4;
  }
  .contact-icon {
    position: absolute;
    left: 765px;
    width: 20px; height: 20px;
  }
</style>
</head>
<body>
  <main class="letterhead">
    <div class="side-band"></div>

    <header class="brand">
      <span class="brand-square"></span>
      <span class="brand-name">Meridian Realty Group</span>
    </header>

    <div class="letter-date">Date, 10 September, 2019</div>

    <section class="letter-body">
      <p>
        <span class="line">This is a sample letter that has been placed to demonstrate typing remat (Your Company). letter-</span>
        <span class="line">head design. When positioned properly, it will serve to work in harmony with all other elements</span>
        <span class="line-last">letterhead. This letterhead design is meant to project an image</span>
      </p>
      <p>
        <span class="line">This letterhead design is meant project an image of professionalism reliability. By using simple</span>
        <span class="line">aligen we have created a very spacious feeling. The simplicity suggest rengththe spaciousnes</span>
        <span class="line-last">contributes h aesthetics the layout. These basic qualities along with the (Your Company)</span>
      </p>
      <p>
        <span class="line">look and helps reinforce the (Your Company) brand. letterhead design is meant to project an image</span>
        <span class="line">p design. When positioned properly, it will serve to work in harmony all the other elements letter-</span>
        <span class="line-last">head. sionalism and reliability.</span>
      </p>
      <p>
        <span class="line">This letterhead design is based on the (Form of your logo) form (Your Company) logo. Each statio-</span>
        <span class="line">nery we have created a very spacious feeling. The simplicity suggests strength the spaciousnes</span>
        <span class="line-last">contribute part of the (Form of your logo).</span>
      </p>
    </section>

    <svg class="signature-mark" role="img" aria-label="Handwritten signature of Daniel Harrow" viewBox="0 0 135 30">
      <rect width="135" height="30" rx="4" fill="var(--signature-tone)" opacity="0.35"/>
    </svg>

    <div class="signatory">
      <div class="signatory-name">Daniel Harrow</div>
      <div class="signatory-role">Manager</div>
    </div>

    <ul class="contact-list">
      <li class="contact-item" style="top:1001px;">Your Address will be here<br>xyz - 123 NY</li>
      <li class="contact-item" style="top:1049px;">info@meridianrealty.com</li>
      <li class="contact-item" style="top:1082px;">00 2222 7580</li>
      <li class="contact-item" style="top:1117px;">www.meridianrealty.com</li>
    </ul>

    <svg class="contact-icon" style="top:1006px;" viewBox="0 0 20 20" aria-hidden="true" fill="none" stroke="#fff" stroke-width="1.3">
      <path d="M10 18 C5 12 4.5 10 4.5 8 A5.5 5.5 0 0 1 15.5 8 C15.5 10 15 12 10 18 Z"/>
      <circle cx="10" cy="8" r="2"/>
    </svg>
    <svg class="contact-icon" style="top:1048px;" viewBox="0 0 20 20" aria-hidden="true" fill="none" stroke="#fff" stroke-width="1.3">
      <rect x="3" y="5" width="14" height="10"/>
      <path d="M3 5 L10 11 L17 5"/>
    </svg>
    <svg class="contact-icon" style="top:1081px;" viewBox="0 0 20 20" aria-hidden="true" fill="none" stroke="#fff" stroke-width="1.3">
      <path d="M7 3 C11 3 13 6 13 9 C13 12 10 13 10 15 C10 17 8 18 7 17"/>
      <path d="M8 7 C9.5 7 10 8 10 9"/>
    </svg>
    <svg class="contact-icon" style="top:1117px;" viewBox="0 0 20 20" aria-hidden="true" fill="none" stroke="#fff" stroke-width="1.3">
      <path d="M6 4 L6 15 L9 12 L11 16.5 L12.6 15.8 L10.6 11.4 L14.5 11.4 Z"/>
    </svg>
  </main>
</body>
</html>
```